Skill Up Salary Up

Full Page
7.5 w x 10 h / 8 w x 10.75 h + .25" bleed
Full-Page Career Course Ad
Project Overview
• Goal: Create a visually attractive, modern, and uncluttered full-page magazine advertisement to list available career courses.
• Tone: Creative, professional, and attention-grabbing to prevent the reader from turning the page. The final design must prioritize readability.

Content Requirements
1. Header/Headline: Must be the primary focus. And grab peoples attention
2. Course Listing: A clear, well-organized list of the career courses.
________________________________________
Design & Aesthetic Directives
1. Layout & Readability (Crucial)
• The final ad must not look crowded or busy.
• Prioritize white space to make the text "breathe" and ensure the course list is easy to scan and read.
• Use a modern, clean, and professional typeface (font choice is critical for the aesthetic).
2. Visual Style
• Aim for a creative, modern, and fresh look. Avoid outdated or generic stock imagery/layouts.
3. Imagery/Graphic Element (Artist's Choice)
You have creative freedom regarding the main graphic element.
• Option A (Photography): Use a photo of a white male American with a collared shirt. The imagery should convey success, focus, or professional development.
• Option B (Vector/Illustration): Use a modern vector graphic, illustration, or abstract design. This could be used to symbolize growth, connection, or a career path.
The choice of graphic element is yours, but it must support the overall modern and uncrowded aesthetic.

Requirements
Must have
• Partial listing .. is part of the Harbor Lantern Course

```html
<!DOCTYPE html>
<html lang="en">
<head>
<meta charset="utf-8">
<title>Skill Up, Salary Up – Upcoming TLM Courses</title>
<link href="https://fonts.googleapis.com/css2?family=Poppins:wght@400;500;600;700&family=Oswald:wght@700&display=swap" rel="stylesheet">
<style>
:root{
  --navy:#1b145c;
  --navy-deep:#120c45;
  --purple:#7b2a8c;
  --orange:#f0a020;
  --ink:#1a1a2a;
  --bar:#cfcfcf;
  --page:#f3f4f8;
  --stage:#4a4a4a;
}
*{box-sizing:border-box;margin:0;padding:0}
html,body{width:1200px;height:1200px;overflow:hidden;background:var(--stage);font-family:"Poppins",sans-serif;color:var(--ink)}
.flyer{position:absolute;left:160px;top:22px;width:880px;height:1155px;background:var(--page);overflow:hidden}
.abs{position:absolute;white-space:nowrap}
.header-band{position:absolute;left:0;top:0;width:880px;height:265px}
.header-visual{position:absolute;right:0;top:0;width:370px;height:236px;background:linear-gradient(100deg,rgba(27,20,92,1) 0%,rgba(30,60,140,.85) 35%,#2c6fc4 70%,#4aa0e6 100%)}
.kicker{left:70px;top:60px;font-weight:600;font-size:33px;color:#fff;letter-spacing:.3px}
.headline{left:68px;top:96px;font-family:"Oswald",sans-serif;font-weight:700;font-size:75px;line-height:1;color:var(--orange);letter-spacing:.5px}
.pill{position:absolute;top:177px;height:31px;background:linear-gradient(90deg,#6e2a93,#8a2a85);color:#fff;font-weight:600;font-size:18.5px;line-height:31px;text-align:center}
.icon-box{position:absolute;width:60px;height:60px;background:var(--navy);border:4px solid #fff;box-shadow:0 0 0 1px #e2e2ea;display:flex;align-items:center;justify-content:center}
.course-title{font-weight:600;font-size:22.5px;line-height:21px;color:var(--navy);text-transform:uppercase}
.sub{font-weight:700;font-size:16.5px;color:var(--purple);line-height:22px}
.body{font-size:15.5px;line-height:20.3px;color:var(--ink)}
.strong{font-weight:600;font-size:17px;color:var(--ink)}
.meta{position:absolute;height:25px;background:var(--bar);font-weight:600;font-size:13px;line-height:25px;text-align:center;color:var(--ink)}
.checks{list-style:none}
.checks li{position:relative;padding-left:17px;font-size:15.5px;line-height:20.3px;white-space:nowrap}
.checks li::before{content:"";position:absolute;left:0;top:6px;width:9px;height:9px;border:1.3px solid var(--orange);border-radius:50%}
.checks li::after{content:"";position:absolute;left:3px;top:7px;width:3px;height:5px;border:solid var(--purple);border-width:0 1.6px 1.6px 0;transform:rotate(40deg)}
.divider{position:absolute;height:0;border-top:1.5px dashed #7a7a88}
.footer{position:absolute;left:0;top:990px;width:880px;height:165px}
.enroll{position:absolute;left:68px;top:1035px;width:271px;height:29px;border-radius:15px;background:var(--orange);color:var(--navy-deep);font-weight:600;font-size:25px;line-height:29px;text-align:center}
.phone{left:122px;top:1068px;font-weight:700;font-size:36px;color:#fff}
.web{left:555px;top:1087px;font-size:24px;color:#fff}
</style>
</head>
<body>
<div class="flyer">
  <svg class="header-band" viewBox="0 0 880 265" aria-hidden="true">
    <defs><linearGradient id="hdr" x1="0" x2="1"><stop offset="0" stop-color="#160f52"/><stop offset="1" stop-color="#2a1f78"/></linearGradient></defs>
    <rect width="880" height="236" fill="url(#hdr)"/>
    <polygon points="0,236 393,236 440,256 487,236 880,236 880,245 487,245 440,262 393,245 0,245" fill="#f0a020"/>
  </svg>
  <div class="header-visual" role="img" aria-label="Glowing technology hexagons with web hosting, code, cloud and gear icons"></div>

  <div class="abs kicker">SKILL UP, SALARY UP</div>
  <div class="abs headline">UPCOMING TLM COURSES</div>
  <div class="pill" style="left:68px;width:180px">MEN &amp; WOMEN</div>
  <div class="pill" style="left:265px;width:239px">IN-PERSON &amp; REMOTE</div>
  <div class="pill" style="left:524px;width:286px">PARTIAL SCHOLARSHIPS</div>

  <!-- Left column: Harbor Lantern -->
  <div class="icon-box" style="left:83px;top:277px">
    <svg width="36" height="36" viewBox="0 0 36 36" fill="none" stroke="#f0a020" stroke-width="2"><circle cx="18" cy="14" r="10"/><ellipse cx="18" cy="14" rx="4" ry="10"/><line x1="8" y1="14" x2="28" y2="14"/><rect x="13" y="25" width="10" height="7" rx="1" fill="#f0a020"/></svg>
  </div>
  <div class="abs course-title" style="left:163px;top:290px">Harbor<br>Lantern</div>
  <div class="abs sub" style="left:83px;top:354px">BUSINESS SKILLS &amp; KNOWLEDGE TO:</div>
  <div class="abs body" style="left:83px;top:384px">Impress your interviewer<br>Maximize Income<br>Start / Run Your Business</div>
  <div class="meta" style="left:84px;top:453px;width:301px">Duration: 4-5 MONTHS &nbsp;|&nbsp; Date: Nov, 2025</div>
  <div class="abs sub" style="left:83px;top:492px">PARTIAL LISTING</div>
  <ul class="checks abs" style="left:83px;top:522px">
    <li>Computers</li><li>Marketing</li><li>Sales</li><li>Finance</li><li>Healthcare</li><li>Business Strategy</li>
  </ul>
  <ul class="checks abs" style="left:254px;top:522px">
    <li>Communication</li><li>LedgerBooks</li><li>Investments</li><li>Real Estate</li><li>Accounting</li>
  </ul>
  <div class="divider" style="left:84px;top:669px;width:301px"></div>

  <div class="icon-box" style="left:83px;top:692px">
    <svg width="36" height="36" viewBox="0 0 36 36" fill="none" stroke="#f0a020" stroke-width="2"><rect x="3" y="5" width="30" height="26" rx="3"/><line x1="3" y1="11" x2="33" y2="11"/><path d="M12 24a4 4 0 0 1 1-8 5 5 0 0 1 9 1 3.5 3.5 0 0 1 1 7z" fill="#f0a020"/></svg>
  </div>
  <div class="abs course-title" style="left:163px;top:713px">Software,<br>Web &amp; Apps</div>
  <div class="abs sub" style="left:83px;top:772px"># 2 BEST TECH JOB</div>
  <div class="abs strong" style="left:83px;top:794px">National Career Review 2025</div>
  <div class="abs sub" style="left:83px;top:825px">JOB OPPORTUNITIES</div>
  <ul class="checks abs" style="left:83px;top:854px">
    <li>Computer Programmer</li><li>Software Developer/Mobile</li><li>Engineer Developer (Apps)</li>
  </ul>
  <div class="abs strong" style="left:83px;top:925px">Optional: Bachelors in Prog. &amp; Tech.</div>
  <div class="meta" style="left:84px;top:962px;width:132px">Date: Nov 2025</div>

  <!-- Right column -->
  <div class="icon-box" style="left:487px;top:271px">
    <svg width="36" height="36" viewBox="0 0 36 36" fill="#f0a020"><rect x="12" y="3" width="20" height="28" rx="2"/><circle cx="11" cy="25" r="8" fill="#1b145c" stroke="#f0a020" stroke-width="2"/><text x="11" y="29.5" font-size="12" font-weight="700" text-anchor="middle" font-family="Poppins,sans-serif">$</text></svg>
  </div>
  <div class="abs course-title" style="left:566px;top:292px">Bookkeeping<br>LedgerBooks</div>
  <div class="abs sub" style="left:487px;top:350px">TRAIN FOR A QUALITY JOB<br>MANAGE YOUR OWN BOOKS</div>
  <ul class="checks abs" style="left:487px;top:404px">
    <li>Finance Management</li><li>Customer &amp; Vendor Mgmt.</li><li>Advanced Tools</li>
  </ul>
  <div class="meta" style="left:487px;top:470px;width:299px">Duration: &nbsp;5 WEEKS &nbsp;|&nbsp; Date: Nov 2025</div>
  <div class="divider" style="left:487px;top:515px;width:299px"></div>

  <div class="icon-box" style="left:487px;top:540px">
    <svg width="38" height="38" viewBox="0 0 38 38" fill="none" stroke="#f0a020" stroke-width="2"><polygon points="19,3 33,11 33,27 19,35 5,27 5,11"/><circle cx="19" cy="19" r="8"/><ellipse cx="19" cy="19" rx="3.5" ry="8"/><line x1="11" y1="19" x2="27" y2="19"/></svg>
  </div>
  <div class="abs course-title" style="left:566px;top:543px">IT Desktop &amp;<br>Networking<br>Support</div>
  <div class="abs sub" style="left:487px;top:618px">#2 BEST JOB</div>
  <div class="abs strong" style="left:487px;top:640px">National Career Review 2025</div>
  <div class="abs sub" style="left:487px;top:674px">MASTERS IT:</div>
  <ul class="checks abs" style="left:487px;top:704px"><li>Desktop OS</li><li>Servers</li></ul>
  <ul class="checks abs" style="left:601px;top:704px"><li>Networks</li><li>Cloud</li></ul>
  <div class="meta" style="left:487px;top:757px;width:299px">Duration: 7 MONTHS &nbsp;|&nbsp; Date: Dec 2025</div>
  <div class="divider" style="left:487px;top:808px;width:299px"></div>

  <div class="icon-box" style="left:487px;top:834px">
    <svg width="30" height="30" viewBox="0 0 30 30"><rect x="3" y="3" width="24" height="24" fill="#f0a020"/></svg>
  </div>
  <div class="abs course-title" style="left:566px;top:845px">Desktop Office<br>Computers</div>
  <div class="abs sub" style="left:487px;top:911px">THE NEW JOB PREREQUISITE</div>
  <ul class="checks abs" style="left:487px;top:942px"><li>Sheets Pro</li><li>Mailbox</li></ul>
  <ul class="checks abs" style="left:596px;top:942px"><li>Writer</li><li>SlideDeck</li></ul>
  <div class="abs" style="left:487px;top:992px;font-weight:600;font-size:14.5px">Computer lab available to practice</div>
  <div class="meta" style="left:487px;top:1026px;width:299px">Duration: 5 Weeks &nbsp;|&nbsp; Date: Dec 2025</div>

  <!-- Footer -->
  <svg class="footer" viewBox="0 990 880 165" aria-hidden="true">
    <defs><linearGradient id="ftr" x1="0" x2="1"><stop offset="0" stop-color="#1d1668"/><stop offset="1" stop-color="#120c45"/></linearGradient></defs>
    <polygon points="0,1000 394,1000 453,1058 880,1058 880,1155 0,1155" fill="#bdbdc6"/>
    <polygon points="0,1009 390,1009 449,1067 880,1067 880,1155 0,1155" fill="url(#ftr)"/>
    <path d="M75 1080c-4 8 2 20 14 26l5-6-6-5-4 3c-4-3-6-7-6-11l4-2-3-7z" fill="#f0a020"/>
    <path d="M88 1080a10 10 0 0 1 9 9M88 1075a15 15 0 0 1 14 14" stroke="#f0a020" stroke-width="2" fill="none"/>
  </svg>
  <div class="enroll">ENROLL TODAY</div>
  <div class="abs phone">555-014-2287</div>
  <div class="abs web">www.tlmcareers.org</div>
</div>
</body>
</html>
```